Medical Services company. Need a website that blows the competition out of the water

We need a web site designed to draw attention to our many services offered. We are a Medical Services business based out of Pennsylvania. We provide basic first aid staffing for events and businesses such as but not limited to: Fairs, Festivals, Carnivals, Sporting events, Large gatherings where a first aid station is needed, Concerts, Businesses with first aid needs . We provide training and certifications that are tailored to the customers needs. We provide Covid-19 pre screening and temperature monitoring. Our professionals consist of individuals with Basic First Aid, Certified Nursing Assistants, Medical Assistants, Emergency Medical Responders (EMR), Emergency Medical Technicians (EMT), and Nurses. I do not know how many pages I will need since we offer multiple different services. Our main services provided are: First Aid services, Covid-19 pre screen and temperatures, and Training/Certifications. You will have to use stock photos for now until I can get some actual photographs of our team.I have uploaded a copy of my brochure so you can get some information from there as well.

Target Market(s)

-For the first Aid and Covid-19 services: All Businesses, Sporting events, Event organizers
-Training: Everyone.

Font styles to use
Sans Serif

Requirements
Must have
• My colors are what is in the logos and Gray , need to have a way for customers to request a quote, design that grabs their attention. Should have pictures of medical providers attending to the sick or injured. Both in a office setting and in an emergency out in public. Should have pictures of an ambulance. Should also have pictures of staff taking temperatures and asking pre screening questions.
Nice to have
• I'll get back to you on that one

```html
<!DOCTYPE html>
<html lang="en">
<head>
<meta charset="utf-8">
<title>Keystone Care Medical</title>
<link rel="stylesheet" href="https://fonts.googleapis.com/css2?family=Poppins:wght@400;500;600;700;800&display=swap">
<style>
:root{
  --navy:#2b2f91;
  --navy-deep:#22267a;
  --teal:#17b3a0;
  --teal-dark:#10988a;
  --ink:#2c2c2c;
  --muted:#777;
  --light:#f4f5f7;
  --line:#e3e5ea;
  --footer:#3c3d3f;
  --footer-deep:#2f3031;
  --white:#fff;
}
*{box-sizing:border-box;margin:0;padding:0}
html,body{width:1200px;height:4980px;overflow:hidden}
body{position:relative;font-family:"Poppins",sans-serif;color:var(--ink);background:var(--white)}
.abs{position:absolute}
.photo{position:absolute;overflow:hidden}
h2.section-title{position:absolute;left:0;width:1200px;text-align:center;font-size:40px;font-weight:700;color:var(--ink)}
.btn{display:inline-block;background:var(--teal);color:var(--white);font-weight:600;font-size:14px;letter-spacing:.5px;border-radius:30px;padding:14px 30px;text-transform:uppercase}

/* header */
.site-header{position:absolute;left:0;top:0;width:1200px;height:112px;background:var(--white)}
.brand{position:absolute;left:88px;top:22px;display:flex;align-items:center;gap:12px}
.brand-dot{width:46px;height:46px;border-radius:50%;background:var(--teal)}
.brand-name{font-size:28px;font-weight:700;color:var(--navy);line-height:1}
.top-contact{position:absolute;top:14px;display:flex;align-items:center;gap:10px;font-size:14px;color:var(--ink)}
.top-contact small{display:block;font-size:11px;color:var(--muted)}
.top-contact .ico{width:26px;height:26px;border-radius:50%;background:var(--teal);display:flex;align-items:center;justify-content:center}
.main-nav{position:absolute;left:512px;top:66px;width:688px;height:46px;background:var(--teal);display:flex;align-items:center;padding-left:40px;gap:42px}
.main-nav a{color:var(--white);font-size:14px;font-weight:600;text-decoration:none;letter-spacing:.5px}

/* hero */
.hero-panel{position:absolute;left:0;top:112px;width:470px;height:668px;background:var(--navy)}
.hero-title{position:absolute;left:88px;top:160px;width:420px;font-size:50px;line-height:1.1;font-weight:700;color:var(--white)}
.hero-text{position:absolute;left:88px;top:420px;width:340px;font-size:15px;line-height:1.6;color:#dfe1f5}
.hero-btn{position:absolute;left:88px;top:560px;font-size:12px;padding:12px 26px}
.scroll-mouse{position:absolute;left:92px;top:700px;width:22px;height:36px;border:2px solid #c9ccef;border-radius:12px}
.scroll-mouse::after{content:"";position:absolute;left:8px;top:7px;width:2px;height:8px;background:#c9ccef;border-radius:2px}

/* we provide */
.provide-title{position:absolute;left:88px;top:938px;font-size:28px;font-weight:700;letter-spacing:1px}
.provide-list{position:absolute;left:88px;top:1020px;display:flex;gap:30px}
.provide-card{width:114px;height:176px;background:var(--white);border-radius:10px;box-shadow:0 6px 22px rgba(0,0,0,.1);padding:22px 14px}
.provide-card svg{display:block;margin:0 auto 22px}
.provide-card p{font-size:13px;line-height:1.35;color:var(--ink)}
.wave-band{position:absolute;left:0;top:1180px;width:1200px;height:160px}

/* medical services */
.service-card{position:absolute;top:1400px}
.service-label{position:absolute;background:var(--white);box-shadow:0 6px 22px rgba(0,0,0,.12);padding:16px 18px;border-top:3px solid var(--teal)}
.service-label h3{font-size:20px;font-weight:600;margin-bottom:6px}
.service-label p{font-size:12px;line-height:1.45;color:var(--muted)}
.services-btn{position:absolute;left:476px;top:1904px}

/* keeping safe */
.dots{position:absolute;width:110px;height:110px;background-image:radial-gradient(#c9cbd6 2px,transparent 2.5px);background-size:14px 14px}
.region-box{position:absolute;left:140px;top:2352px;width:248px;height:138px;background:var(--navy);padding:22px 22px;color:var(--white)}
.region-box h4{font-size:17px;font-weight:600;line-height:1.35;margin-bottom:14px}
.region-box span{font-size:12px}
.safe-title{position:absolute;left:680px;top:2250px;font-size:40px;font-weight:700}
.bullets{list-style:none}
.bullets li{position:relative;padding-left:20px;margin-bottom:14px;font-size:13px;line-height:1.55}
.bullets li::before{content:"";position:absolute;left:2px;top:8px;width:7px;height:7px;border-radius:50%;background:var(--teal)}
.safe-list{position:absolute;left:680px;top:2340px;width:460px;color:var(--muted)}

/* training */
.training-band{position:absolute;left:0;top:2660px;width:1200px;height:680px}
.training-title{position:absolute;left:130px;top:2800px;font-size:40px;font-weight:700;color:var(--white)}
.training-list{position:absolute;left:130px;top:2880px;width:440px;color:var(--white)}
.training-list li::before{background:var(--white)}

/* testimonials */
.quote-text{position:absolute;left:300px;top:3540px;width:600px;text-align:center;font-size:14px;line-height:1.7;color:var(--muted)}
.quote-author{position:absolute;left:0;width:1200px;top:3628px;text-align:center;font-size:18px;font-weight:600;color:var(--teal)}
.avatar{position:absolute;border-radius:50%;border:3px solid var(--white);box-shadow:0 3px 10px rgba(0,0,0,.15);background:linear-gradient(135deg,#c9a27e,#8c6a51)}
.arrow-btn{position:absolute;top:3690px;width:44px;height:44px;border-radius:50%;display:flex;align-items:center;justify-content:center}

/* events */
.footer-bg{position:absolute;left:0;top:4260px;width:1200px;height:720px}
.event-card{position:absolute;top:3938px;width:502px;height:420px;background:var(--white);border-radius:14px;box-shadow:0 8px 28px rgba(0,0,0,.14);overflow:hidden}
.event-card .photo{left:0;top:0;width:502px;height:230px}
.event-body{position:absolute;left:22px;top:246px;width:458px}
.event-meta{font-size:11px;color:var(--muted);margin-bottom:10px}
.event-body h3{font-size:20px;font-weight:600;margin-bottom:8px}
.event-body p{font-size:12px;line-height:1.5;color:var(--muted);margin-bottom:10px}
.read-link{font-size:13px;font-weight:600;color:var(--teal)}

/* footer */
.footer-brand{position:absolute;left:120px;top:4530px;display:flex;align-items:center;gap:12px}
.footer-brand .brand-name{color:var(--white);font-size:26px}
.footer-col{position:absolute;top:4500px;color:var(--white)}
.footer-col h5{font-size:16px;font-weight:600;margin-bottom:14px}
.footer-col li{list-style:none;font-size:13px;line-height:1.75;color:#d6d6d6}
.contact-row{display:flex;gap:12px;margin-bottom:18px;font-size:13px;color:#d6d6d6}
.contact-row small{display:block;font-size:11px;color:#aaa}
.social{display:flex;gap:12px;margin-top:6px}
.social span{width:30px;height:30px;border-radius:50%;border:1px solid #8a8a8a}
.copyright{position:absolute;left:0;top:4928px;width:1200px;height:52px;background:var(--footer-deep);color:#cfcfcf;font-size:12px;text-align:center;line-height:52px}
.to-top{position:absolute;left:1128px;top:4880px;width:40px;height:40px;border-radius:50%;background:var(--teal)}
</style>
</head>
<body>

<header class="site-header">
  <div class="brand"><span class="brand-dot"></span><span class="brand-name">Keystone Care</span></div>
  <div class="top-contact" style="left:720px">
    <span class="ico"><svg width="13" height="13" viewBox="0 0 24 24"><path fill="#fff" d="M6.6 10.8a15 15 0 006.6 6.6l2.2-2.2a1 1 0 011-.25 11 11 0 003.5.56 1 1 0 011 1V20a1 1 0 01-1 1A17 17 0 013 4a1 1 0 011-1h3.5a1 1 0 011 1 11 11 0 00.56 3.5 1 1 0 01-.25 1z"/></svg></span>
    <div><small>Call</small>555-014-2290</div>
  </div>
  <div class="top-contact" style="left:900px">
    <span class="ico"><svg width="13" height="13" viewBox="0 0 24 24"><circle cx="12" cy="12" r="9" fill="none" stroke="#fff" stroke-width="2"/><path d="M3 12h18M12 3c3 3 3 15 0 18M12 3c-3 3-3 15 0 18" fill="none" stroke="#fff" stroke-width="1.6"/></svg></span>
    <div><small>Website</small>www.keystonecaremed.com</div>
  </div>
  <nav class="main-nav">
    <a>HOME</a><a>ABOUT</a><a>SERVICES</a><a>TRAINING</a><a>BLOG</a><a>CONTACT US</a>
  </nav>
</header>

<section class="hero">
  <div class="photo" role="img" aria-label="Paramedic checking a seated patient's blood pressure inside an ambulance" style="left:440px;top:112px;width:760px;height:650px;background:linear-gradient(120deg,#d9dde3 0%,#9aa7b4 40%,#5c6f86 75%,#c7a487 100%)"></div>
  <svg class="abs" style="left:0;top:700px" width="1200" height="90" viewBox="0 0 1200 90" preserveAspectRatio="none"><path d="M0 90V60Q600 100 1200 20V90Z" fill="#fff"/></svg>
  <div class="hero-panel"></div>
  <h1 class="hero-title">Providing all of your health and safety needs</h1>
  <p class="hero-text">We will give you the confidence that your community and staff are healthy and safe.</p>
  <a class="btn hero-btn">Request a Quote</a>
  <span class="scroll-mouse"></span>
</section>

<section class="provide">
  <h2 class="provide-title">WE PROVIDE</h2>
  <div class="provide-list">
    <div class="provide-card"><svg width="44" height="44" viewBox="0 0 44 44" fill="none" stroke="#2b2f91" stroke-width="2"><path d="M8 38l8-20 10 10z"/><path d="M26 10v6M32 14l-4 4M36 22h-6" stroke="#17b3a0"/></svg><p>Special Events</p></div>
    <div class="provide-card"><svg width="44" height="44" viewBox="0 0 44 44" fill="none" stroke="#2b2f91" stroke-width="2"><circle cx="22" cy="22" r="16"/><circle cx="22" cy="16" r="4" stroke="#17b3a0"/><path d="M14 30c2-5 14-5 16 0"/></svg><p>Large Gatherings</p></div>
    <div class="provide-card"><svg width="44" height="44" viewBox="0 0 44 44" fill="none" stroke="#2b2f91" stroke-width="2"><rect x="8" y="8" width="22" height="28" rx="2"/><path d="M13 16h12M13 22h12M13 28h8"/><circle cx="32" cy="32" r="6" stroke="#17b3a0"/></svg><p>Our Business</p></div>
    <div class="provide-card"><svg width="44" height="44" viewBox="0 0 44 44" fill="none" stroke="#2b2f91" stroke-width="2"><rect x="6" y="10" width="32" height="26" rx="2"/><path d="M6 18h32"/><path d="M18 24h8M22 20v8" stroke="#17b3a0"/></svg><p>Sports Events</p></div>
    <div class="provide-card"><svg width="44" height="44" viewBox="0 0 44 44" fill="none" stroke="#2b2f91" stroke-width="2"><path d="M6 38V20l8 5v-5l8 5v-5l8 5V8h6v30z"/><path d="M12 32h4M20 32h4" stroke="#17b3a0"/></svg><p>Manufacturing Facilities</p></div>
    <div class="provide-card"><svg width="44" height="44" viewBox="0 0 44 44" fill="none" stroke="#2b2f91" stroke-width="2"><rect x="10" y="6" width="16" height="32"/><rect x="26" y="16" width="10" height="22"/><path d="M14 12h8M14 18h8M14 24h8" stroke="#17b3a0"/></svg><p>Industrial Buildings</p></div>
    <div class="provide-card"><svg width="44" height="44" viewBox="0 0 44 44" fill="none" stroke="#2b2f91" stroke-width="2"><path d="M10 38V10h4v28M6 38h12M14 10l22 8M14 14l18 4"/><path d="M32 18v10" stroke="#17b3a0"/></svg><p>Large Construction</p></div>
  </div>
  <svg class="wave-band" viewBox="0 0 1200 160" preserveAspectRatio="none"><path d="M0 40Q300 120 620 60T1200 30V160H0Z" fill="#f4f5f7"/></svg>
</section>

<section class="services abs" style="left:0;top:1290px;width:1200px;height:730px;background:var(--light)"></section>
<h2 class="section-title" style="top:1316px">Medical Services</h2>

<div class="photo" role="img" aria-label="Responders giving first aid to an injured person" style="left:88px;top:1460px;width:362px;height:370px;background:linear-gradient(135deg,#b6463f,#e5e1dc 55%,#7c8794)"></div>
<div class="service-label" style="left:138px;top:1400px;width:286px;height:110px"><h3>First Aid</h3><p>For patients with minor to life threatening injuries or illness...</p></div>

<div class="photo" role="img" aria-label="Medical team performing onsite care on a patient" style="left:500px;top:1400px;width:362px;height:320px;background:linear-gradient(135deg,#7f7570,#c6c9cf 50%,#4e5a6a)"></div>
<div class="service-label" style="left:500px;top:1660px;width:326px;height:176px"><h3>Onsite Care</h3><p>Provide immediate care by ensuring the safety in response ...</p></div>

<div class="photo" role="img" aria-label="Paramedics moving a patient on a stretcher for resuscitation" style="left:912px;top:1460px;width:288px;height:370px;background:linear-gradient(135deg,#d9a44c,#8e99a6 55%,#5b6877)"></div>
<div class="service-label" style="left:952px;top:1400px;width:248px;height:110px"><h3>Trauma/Resuscitation</h3><p>Provide immediate and life saving treatment to patients with...</p></div>

<a class="btn services-btn" style="font-size:12px">View all medical services</a>

<section class="safe">
  <div class="dots" style="left:120px;top:2400px"></div>
  <div class="photo" role="img" aria-label="Nurse with stethoscope attending a patient in an office" style="left:200px;top:2056px;width:400px;height:430px;background:linear-gradient(135deg,#e9ecef,#a9c4c9 50%,#4d8c99)"></div>
  <div class="region-box"><h4>Providing services throughout Pennsylvania</h4><span>Explore Now</span></div>
  <h2 class="safe-title">Keeping Your Safe</h2>
  <ul class="bullets safe-list">
    <li>You will notice the difference when you choose our team for your business or event.</li>
    <li>By having trained, professional responders present, your staff will feel safer and morale will improve, productivity will increase, and incidents will reduce.</li>
    <li>Our goal is to provide the best care and coverage to our customers and patients.</li>
    <li>We are passionate about people and will strive to keep everyone healthy and safe.</li>
  </ul>
</section>

<section class="training">
  <svg class="training-band" viewBox="0 0 1200 680" preserveAspectRatio="none"><path d="M0 30Q600 -20 1200 40V640Q600 700 0 650Z" fill="#17b3a0"/></svg>
  <h2 class="training-title">Training Services</h2>
  <ul class="bullets training-list">
    <li>At our school, we have a broad range of health and safety classes to suit your every need. We use state-of-the-art training with instructors who have years of experience instructing quality courses.</li>
    <li>We make learning CPR fun and affordable for the everyday public and healthcare providers.</li>
    <li>All CPR instruction follows the latest national heart and safety guidelines, the leaders in cardiac research.</li>
    <li>We can adjust any course format to suit your CPR and first aid needs.</li>
  </ul>
  <div class="photo" role="img" aria-label="Large decorative emergency care graphic with a figure at its center" style="left:600px;top:2760px;width:360px;height:440px;border-radius:20px;background:radial-gradient(circle at 50% 45%,#1f8f84,#0f7a70 70%,#17b3a0)"></div>
</section>

<section class="testimonials">
  <h2 class="section-title" style="top:3348px">Client's Testimonials</h2>
  <svg class="abs" style="left:560px;top:3440px" width="80" height="70" viewBox="0 0 80 70"><path d="M4 66V38Q4 8 34 4v12Q20 20 20 36h14v30zM46 66V38Q46 8 76 4v12Q62 20 62 36h14v30z" fill="#eceef1"/></svg>
  <p class="quote-text">Aenean imperdiet etiam ultricies nisl vel augue curabitur ullamcorper ultricies nisi nam eget dui etiam rhoncus maecenas tempus.</p>
  <div class="quote-author">-Jane Rowe</div>
  <div class="arrow-btn" style="left:546px;background:#eceef1"><svg width="14" height="14" viewBox="0 0 14 14"><path d="M9 2L4 7l5 5" fill="none" stroke="#2c2c2c" stroke-width="2"/></svg></div>
  <div class="arrow-btn" style="left:606px;background:var(--ink)"><svg width="14" height="14" viewBox="0 0 14 14"><path d="M5 2l5 5-5 5" fill="none" stroke="#fff" stroke-width="2"/></svg></div>
  <div class="avatar" role="img" aria-label="Client portrait" style="left:100px;top:3412px;width:44px;height:44px"></div>
  <div class="avatar" role="img" aria-label="Client portrait" style="left:0;top:3496px;width:56px;height:56px"></div>
  <div class="avatar" role="img" aria-label="Client portrait" style="left:150px;top:3500px;width:40px;height:40px"></div>
  <div class="avatar" role="img" aria-label="Client portrait" style="left:60px;top:3600px;width:60px;height:60px"></div>
  <div class="avatar" role="img" aria-label="Client portrait" style="left:1056px;top:3420px;width:44px;height:44px"></div>
  <div class="avatar" role="img" aria-label="Client portrait" style="left:1160px;top:3490px;width:56px;height:56px"></div>
  <div class="avatar" role="img" aria-label="Client portrait" style="left:1010px;top:3520px;width:40px;height:40px"></div>
  <div class="avatar" role="img" aria-label="Client portrait" style="left:1090px;top:3600px;width:58px;height:58px"></div>
</section>

<svg class="footer-bg" viewBox="0 0 1200 720" preserveAspectRatio="none"><path d="M0 120Q700 -60 1200 90V720H0Z" fill="#3c3d3f"/></svg>

<section class="events">
  <h2 class="section-title" style="top:3826px">Upcoming Events</h2>
  <article class="event-card" style="left:88px">
    <div class="photo" role="img" aria-label="Ambulance parked at an event"  style="background:linear-gradient(135deg,#dfe6ec,#a8b8c6 55%,#4f6d86)"></div>
    <div class="event-body">
      <div class="event-meta">BY ADMIN &nbsp;•&nbsp; 20 APRIL 2021</div>
      <h3>Some Blog Heading Goes here...</h3>
      <p>Imperdiet etiam ultricies nisi vel augue curabitur ullamcorper ultricies nisi nam eget dui etiam rhoncus maecenas tempus.</p>
      <span class="read-link">READ</span>
    </div>
  </article>
  <article class="event-card" style="left:620px">
    <div class="photo" role="img" aria-label="Masked staff member taking a temperature reading at an entrance" style="background:linear-gradient(135deg,#c8d6e2,#7f9bb4 55%,#2f4d6b)"></div>
    <div class="event-body">
      <div class="event-meta">BY ADMIN &nbsp;•&nbsp; 20 APRIL 2021</div>
      <h3>Some Blog Heading Goes here...</h3>
      <p>Imperdiet etiam ultricies nisi vel augue curabitur ullamcorper ultricies nisi nam eget dui etiam rhoncus maecenas tempus.</p>
      <span class="read-link">READ</span>
    </div>
  </article>
</section>

<footer>
  <div class="footer-brand"><span class="brand-dot"></span><span class="brand-name">Keystone Care</span></div>
  <div class="footer-col" style="left:420px"><h5>Quick Links</h5><ul><li>Home</li><li>About</li><li>Services</li><li>Training</li><li>Blog</li><li>Our Staff</li><li>Contact Us</li></ul></div>
  <div class="footer-col" style="left:600px"><h5>Information</h5><ul><li>Case Studies</li><li>Integration</li><li>FAQ</li><li>Request Demo</li></ul></div>
  <div class="footer-col" style="left:784px"><h5>Contact Info</h5>
    <div class="contact-row"><svg width="22" height="22" viewBox="0 0 24 24"><rect x="3" y="5" width="18" height="14" rx="2" fill="#17b3a0"/><path d="M3 7l9 6 9-6" fill="none" stroke="#fff" stroke-width="1.6"/></svg><div><small>Email</small>hello@keystonecaremed.com</div></div>
    <div class="contact-row"><svg width="22" height="22" viewBox="0 0 24 24"><path fill="#17b3a0" d="M6.6 10.8a15 15 0 006.6 6.6l2.2-2.2a1 1 0 011-.25 11 11 0 003.5.56 1 1 0 011 1V20a1 1 0 01-1 1A17 17 0 013 4a1 1 0 011-1h3.5a1 1 0 011 1 11 11 0 00.56 3.5 1 1 0 01-.25 1z"/></svg><div><small>Phone</small>555-014-2290</div></div>
    <div class="social"><span></span><span></span><span></span><span></span></div>
  </div>
  <span class="to-top"></span>
  <div class="copyright">Copyright © Keystone Care Medical 2021. All Rights Reserved.</div>
</footer>

</body>
</html>
```